Website design 5 pages + short Video + basic graphic optimization for a luxury Homestay - Resort website

I just need the website design for the main pages and optimised graphic images. The website will be mainly based on the following single-page scroll theme.

https://marquinstudio.com/demo/guesthouse-one-page/
FIGMA Templates https://marquinstudio.com/free-figma-design-files-for-hotel-and-vacation-rentals/
You can use these templates as a starting point but create something unique and luxurious.

Find all graphics files here :
1 https://www.storvanta.com/sc/k7q519wp4t2m8r5/AAHJ_Pwoxe47lu829Gbnczq3e
2 https://www.storvanta.com/sh/qmtrk61hxwedzpa/AAC8VolRUM5X7wGHP2NK4ejsu?dl=0

The following is the output :
1. Create website design ( Output high-quality PSD and JPEG files )
a. Homepage ( Example https://marquinstudio.com/demo/countryside2/ )
b. Blog ( Example https://marquinstudio.com/demo/countryside2/blog-2/ )
c. Packages ….. ( Example xxxxx )
d. Room ( Example https://marquinstudio.com/demo/guesthouse-one-page/accommodation/ravelo/ )
e. About us ( Example xxxxx )
f. Contact with embedded google maps ( Example https://marquinstudio.com/demo/hotelclassic/contact-2/ )

2. Short Video edit – 30 to 50 seconds

3. Optimise graphics for all pages and galleries ready to be used in the website ( Output high-quality JPEG files )

```html
<!DOCTYPE html>
<html lang="en">
<head>
<meta charset="utf-8">
<title>Saffron Ridge – Homestay Resort</title>
<link href="https://fonts.googleapis.com/css2?family=Libre+Baskerville&family=Montserrat:wght@400;500;600&family=Great+Vibes&display=swap" rel="stylesheet">
<style>
:root{
  --gold:#f9c053;
  --gold-soft:#fbd27e;
  --ink:#222222;
  --text:#5d5d5d;
  --muted:#8b8b8b;
  --dark:#1c1b19;
  --footer:#272727;
  --white:#ffffff;
  --line:#e6e6e6;
}
*{margin:0;padding:0;box-sizing:border-box}
html,body{width:1200px;height:4179px;overflow:hidden}
body{position:relative;background:var(--white);font-family:"Montserrat",sans-serif;color:var(--text)}
.abs{position:absolute}
.script{font-family:"Great Vibes",cursive;color:var(--gold);font-size:30px;text-align:center}
.section-title{font-family:"Libre Baskerville",serif;font-size:24px;color:var(--ink);text-align:center;letter-spacing:.3px;white-space:nowrap}
.photo{position:absolute}
.btn-outline{position:absolute;border:1.5px solid var(--gold);font-size:12px;font-weight:600;color:var(--ink);display:flex;align-items:center;justify-content:center;letter-spacing:.4px}
.dots{position:absolute;display:flex;gap:8px;justify-content:center;left:0;width:1200px}
.dots span{width:7px;height:7px;border-radius:50%;background:#9a9a9a}
.dots span.on{background:var(--gold)}

/* Hero */
.hero{position:absolute;left:0;top:0;width:1200px;height:560px;background:linear-gradient(180deg,#6f7f5a 0%,#4f6140 35%,#5b4630 65%,#3e2a1e 100%)}
.hero-shade{position:absolute;inset:0;background:rgba(0,0,0,.28)}
.nav{position:absolute;left:157px;top:29px;width:886px;height:68px;background:var(--white);display:flex;align-items:center}
.brand{position:absolute;left:40px;font-family:"Libre Baskerville",serif;font-size:20px;color:var(--gold)}
.menu{position:absolute;left:235px;display:flex;font-size:12px;color:var(--ink)}
.menu a{text-decoration:none;color:var(--ink);margin-right:36px}
.menu a.active{color:var(--gold);border-bottom:1px solid var(--gold);padding-bottom:2px}
.book-now{position:absolute;right:45px;width:100px;height:34px;background:var(--gold);color:var(--white);font-size:12px;display:flex;align-items:center;justify-content:center}
.hero-title{position:absolute;left:0;top:208px;width:1200px;text-align:center;color:var(--white);font-family:"Libre Baskerville",serif;font-weight:400;font-size:38px;line-height:58px}
.hero-sub{position:absolute;left:0;top:344px;width:1200px;text-align:center;color:var(--white);font-size:14px;line-height:19px}
.search{position:absolute;left:276px;top:454px;width:650px;height:81px;background:rgba(20,18,15,.55)}
.field{position:absolute;top:18px;color:var(--white);font-size:12px;font-weight:500}
.field .box{margin-top:8px;width:110px;height:20px;border:1px solid #c9c9c9;font-size:10px;font-weight:400;color:#ddd;padding:0 6px;display:flex;align-items:center;justify-content:space-between}
.search-btn{position:absolute;right:0;top:0;width:95px;height:81px;background:var(--gold);color:var(--white);font-size:12px;font-weight:600;display:flex;align-items:center;justify-content:center}

/* About */
.about-label{position:absolute;left:646px;top:642px;text-align:left;white-space:nowrap}
.about-text{position:absolute;left:632px;top:690px;width:420px}
.about-text h2{font-family:"Libre Baskerville",serif;font-weight:400;font-size:20px;line-height:36px;color:var(--ink);white-space:nowrap}
.about-text p{margin-top:8px;font-size:15px;line-height:24px;color:var(--text);white-space:nowrap}

/* Travel */
.travel{position:absolute;left:0;top:1148px;width:1200px;height:690px;background:linear-gradient(180deg,#23211d,#161513 60%,#1f1c18)}
.arrow{position:absolute}

/* Services */
.card{position:absolute;top:2019px;width:189px;height:171px;border:1px solid var(--line);background:var(--white);padding:24px 0 0 27px}
.card.dark{background:var(--dark);border-color:var(--dark)}
.card h3{font-family:"Libre Baskerville",serif;font-weight:400;font-size:17px;color:var(--ink);margin-top:14px;white-space:nowrap}
.card.dark h3{color:var(--gold)}
.card p{font-size:11.5px;line-height:17px;color:var(--muted);margin-top:6px;width:140px}
.card.dark p{color:#ddd}
.card .more{font-size:11px;font-style:italic;color:var(--muted);margin-top:8px;display:flex;align-items:center;gap:5px}
.card.dark .more{color:var(--gold)}
.card svg.icon{display:block}

/* Video band */
.video{position:absolute;left:0;top:2251px;width:1200px;height:422px;background:linear-gradient(180deg,#3f6a86 0%,#5c7b8e 45%,#3f5466 75%,#2f3d4a 100%)}
.video-title{position:absolute;left:0;top:96px;width:1200px;text-align:center;font-family:"Libre Baskerville",serif;font-size:23px;color:var(--gold)}

/* Rooms */
.room-name{position:absolute;top:3098px;font-family:"Libre Baskerville",serif;font-size:18px;color:var(--ink);white-space:nowrap}
.room-desc{position:absolute;top:3136px;width:250px;font-size:14px;line-height:18px;color:var(--muted)}
.room-price{position:absolute;top:3204px;font-size:18px;font-weight:600;color:var(--gold-soft);white-space:nowrap}

/* Testimonial */
.quote{position:absolute;left:0;top:3428px;width:1200px;text-align:center;font-size:17px;line-height:22px;color:var(--text)}
.quote-name{position:absolute;left:0;top:3498px;width:1200px;text-align:center;font-family:"Libre Baskerville",serif;font-size:15px;color:var(--ink)}

/* Footer */
.footer{position:absolute;left:0;top:3693px;width:1200px;height:486px;background:var(--footer)}
.footer-brand{position:absolute;left:516px;top:78px;width:165px;height:122px;display:flex;align-items:center;justify-content:center;font-family:"Libre Baskerville",serif;font-size:19px;color:var(--gold);white-space:nowrap}
.news{position:absolute;left:0;top:254px;width:1200px;text-align:center;font-family:"Libre Baskerville",serif;font-size:17px;color:var(--gold)}
.news-input{position:absolute;left:441px;top:297px;width:316px;height:32px;border:1px solid #8a8a8a;font-size:9px;color:#cfcfcf;padding-left:12px;display:flex;align-items:center}
.socials{position:absolute;left:0;top:370px;width:1200px;display:flex;justify-content:center;gap:18px}
.socials span{width:14px;height:14px;background:#e8e8e8;border-radius:2px}
.socials span.hl{background:var(--gold)}
.copy{position:absolute;left:0;top:425px;width:1200px;text-align:center;font-size:8px;color:var(--gold)}
</style>
</head>
<body>

<!-- Hero -->
<header class="hero" role="img" aria-label="Guesthouse veranda with hanging plants overlooking forested hills">
  <div class="hero-shade"></div>
  <nav class="nav">
    <div class="brand">Saffron Ridge</div>
    <div class="menu">
      <a class="active">Home</a><a>About us</a><a>Room</a><a>Page</a><a>Blog</a><a>Contact Us</a>
    </div>
    <div class="book-now">Book Now</div>
  </nav>
  <h1 class="hero-title">SPEND YOUR HOLIDAY IN<br>OUR BEATIFULL PLACE</h1>
  <p class="hero-sub">Lorem ipsum dolor sit amet, consectetur adipiscing elit,sed do eiusmod<br>tempor incididunt ut labore et dolore agna aliqua.</p>
  <form class="search">
    <div class="field" style="left:24px">ARRIVAL DATE<div class="box">Arrival Date <span>▦</span></div></div>
    <div class="field" style="left:167px">DEPARTURE DATE<div class="box">Arrival Date <span>▦</span></div></div>
    <div class="field" style="left:318px">ADULS<div class="box">Arrival Date <span>⌄</span></div></div>
    <div class="field" style="left:445px">CHILDREN<div class="box">Children <span>⌄</span></div></div>
    <div class="search-btn">SERCH</div>
  </form>
</header>

<!-- About -->
<section>
  <div class="abs" style="left:247px;top:681px;width:39px;height:44px;background:var(--gold)"></div>
  <div class="abs" style="left:247px;top:993px;width:39px;height:50px;background:var(--gold)"></div>
  <div class="photo" style="left:284px;top:652px;width:302px;height:414px;background:linear-gradient(160deg,#3a2a18,#b8741e 45%,#6a3d12 70%,#1a140e)" role="img" aria-label="Wooden A-frame cottage glowing with warm lights at dusk"></div>
  <div class="abs" style="left:193px;top:725px;width:221px;height:268px;background:#f1f1f1"></div>
  <div class="photo" style="left:203px;top:736px;width:202px;height:246px;background:linear-gradient(180deg,#7fb1e4 0%,#6f9a5c 40%,#3f6e2e 75%,#2c5020)" role="img" aria-label="Green-roofed cottage surrounded by trees"></div>
  <div class="script about-label">About Saffron Ridge</div>
  <div class="about-text">
    <h2>WELCOME TO THE SAFFRON RIDGE<br>USE ENJOY AND GET INSPIRED.</h2>
    <p>Lorem ipsum dolor sit amet, consectetur adipi<br>scing elit, sed do eiusmod tempor labore</p>
  </div>
  <div class="photo" style="left:628px;top:839px;width:175px;height:225px;background:linear-gradient(170deg,#e8c9b4,#c99b86 50%,#8a5f52)" role="img" aria-label="Cosy guest room with low bed and curtains"></div>
  <div class="btn-outline" style="left:835px;top:856px;width:130px;height:36px">ABOUT US</div>
</section>

<!-- Top Travel Places -->
<section class="travel">
  <div class="script abs" style="left:0;top:48px;width:1200px">Top Travel Places</div>
  <div class="section-title abs" style="left:0;top:118px;width:1200px;color:var(--white)">INCREDIBTY BEAUTIFUL NATURE IS LOCATED NEXT TO US</div>
  <svg class="arrow" style="left:14px;top:317px" width="14" height="26" viewBox="0 0 14 26"><path d="M12 2 2 13l10 11" fill="none" stroke="#cfcfcf" stroke-width="1.5"/></svg>
  <svg class="arrow" style="left:1168px;top:317px" width="14" height="26" viewBox="0 0 14 26"><path d="M2 2l10 11L2 24" fill="none" stroke="#cfcfcf" stroke-width="1.5"/></svg>
  <div class="photo" style="left:73px;top:197px;width:255px;height:324px;background:linear-gradient(180deg,#4f86d6 0%,#8fb6e0 25%,#3f7a33 50%,#6aa34a 100%)" role="img" aria-label="Guests walking across a green lawn with dogs"></div>
  <div class="photo" style="left:341px;top:197px;width:254px;height:324px;background:linear-gradient(180deg,#3f6a2c 0%,#5b6a55 35%,#7a7e80 65%,#3c3e40 100%)" role="img" aria-label="Friends wading in a mountain stream"></div>
  <div class="photo" style="left:605px;top:197px;width:255px;height:324px;background:linear-gradient(180deg,#2f7fd8 0%,#6aa3e0 45%,#9db6cf 65%,#5b6a6a 100%)" role="img" aria-label="Snowy mountain range beyond flowering shrubs"></div>
  <div class="photo" style="left:871px;top:197px;width:255px;height:324px;background:linear-gradient(180deg,#e3ecf2 0%,#a9c3b2 30%,#5f8f3c 60%,#c7c82a 100%)" role="img" aria-label="Terraced green hills with yellow leaves in front"></div>
  <div class="dots" style="top:559px"><span class="on"></span><span></span><span class="on"></span><span></span></div>
  <div class="btn-outline" style="left:530px;top:609px;width:138px;height:37px;color:var(--white);border-color:#d9d9d9">VIEW MORE</div>
</section>

<!-- Services -->
<section>
  <div class="script abs" style="left:0;top:1872px;width:1200px">Our Service</div>
  <div class="section-title abs" style="left:0;top:1935px;width:1200px">LUXURY AND BEST SERVICE SAFFRON RIDGE IN THE</div>

  <div class="card dark" style="left:201px">
    <svg class="icon" width="46" height="30" viewBox="0 0 46 30" fill="none" stroke="#f9c053" stroke-width="1.5"><path d="M4 14h38M8 14v14M38 14v14M16 14l-3 14M30 14l3 14"/><path d="M15 10a8 8 0 0 1 16 0"/><path d="M23 2v2M6 2v8M3 2v5M9 2v5M40 2v8"/></svg>
    <h3>Restaurant</h3>
    <p>Lorem ipsum dolor sit amet, consectetur</p>
    <div class="more">Read More <svg width="12" height="8" viewBox="0 0 12 8"><path d="M0 4h10M7 1l3 3-3 3" fill="none" stroke="currentColor"/></svg></div>
  </div>
  <div class="card" style="left:404px">
    <svg class="icon" width="46" height="30" viewBox="0 0 46 30" fill="none" stroke="#333" stroke-width="1.5"><circle cx="30" cy="6" r="3.5"/><path d="M8 16l10-8 6 6"/><path d="M4 22c4-3 7 3 11 0s7 3 11 0 7 3 11 0"/><path d="M4 27c4-3 7 3 11 0s7 3 11 0 7 3 11 0"/></svg>
    <h3>Swiming Pool</h3>
    <p>Lorem ipsum dolor sit amet, consectetur</p>
    <div class="more">Read More <svg width="12" height="8" viewBox="0 0 12 8"><path d="M0 4h10M7 1l3 3-3 3" fill="none" stroke="currentColor"/></svg></div>
  </div>
  <div class="card" style="left:607px">
    <svg class="icon" width="46" height="30" viewBox="0 0 46 30" fill="none" stroke="#333" stroke-width="1.5"><path d="M6 18c6 0 10-6 18-6 5 0 8 3 8 6s-4 5-9 5H12"/><path d="M26 6c3-4 9-3 9 2s-6 7-9 9c-3-2-9-4-9-9s6-6 9-2z"/></svg>
    <h3>Health &amp; Beauty</h3>
    <p>Lorem ipsum dolor sit amet, consectetur</p>
    <div class="more">Read More <svg width="12" height="8" viewBox="0 0 12 8"><path d="M0 4h10M7 1l3 3-3 3" fill="none" stroke="currentColor"/></svg></div>
  </div>
  <div class="card" style="left:809px">
    <svg class="icon" width="46" height="30" viewBox="0 0 46 30" fill="none" stroke="#333" stroke-width="1.5"><rect x="4" y="2" width="24" height="16"/><circle cx="16" cy="10" r="2.5"/><path d="M4 24h34M6 28h4M14 28h4M22 28h4M30 28h4"/></svg>
    <h3>Conference Room</h3>
    <p>Lorem ipsum dolor sit amet, consectetur</p>
    <div class="more">Read More <svg width="12" height="8" viewBox="0 0 12 8"><path d="M0 4h10M7 1l3 3-3 3" fill="none" stroke="currentColor"/></svg></div>
  </div>
</section>

<!-- Video band -->
<section class="video" role="img" aria-label="Pink blossoms in front of snow-capped mountains under a blue sky">
  <div class="video-title">ENJOY YOUR DREAM VACATION</div>
  <svg class="abs" style="left:558px;top:168px" width="84" height="84" viewBox="0 0 84 84" fill="none" stroke="#ffffff" stroke-width="4"><path d="M42 4a38 38 0 1 1-30 14"/><path d="M33 26v32l24-16z" stroke-linejoin="round"/></svg>
</section>

<!-- Rooms -->
<section>
  <div class="script abs" style="left:0;top:2718px;width:1200px">Room Type</div>
  <div class="section-title abs" style="left:0;top:2770px;width:1200px">OUR COMFORT ROOM</div>
  <svg class="arrow" style="left:30px;top:2940px" width="14" height="26" viewBox="0 0 14 26"><path d="M12 2 2 13l10 11" fill="none" stroke="#888" stroke-width="1.5"/></svg>
  <svg class="arrow" style="left:1156px;top:2940px" width="14" height="26" viewBox="0 0 14 26"><path d="M2 2l10 11L2 24" fill="none" stroke="#f9c053" stroke-width="1.5"/></svg>

  <div class="photo" style="left:201px;top:2845px;width:256px;height:230px;background:linear-gradient(180deg,#e9e39a 0%,#dcd47e 60%,#c8a23a 100%)" role="img" aria-label="Single room with yellow bed and framed pictures"></div>
  <div class="photo" style="left:470px;top:2845px;width:257px;height:230px;background:linear-gradient(180deg,#e6d67c 0%,#d8c26a 55%,#8f6a35 100%)" role="img" aria-label="Family room with green door and wooden dresser"></div>
  <div class="photo" style="left:741px;top:2845px;width:257px;height:230px;background:linear-gradient(180deg,#f0e08c 0%,#e8d79a 50%,#c9c7b6 100%)" role="img" aria-label="Standard room with kitchenette counter"></div>

  <div class="room-name" style="left:201px">Singal Room</div>
  <div class="room-name" style="left:470px">Family Room</div>
  <div class="room-name" style="left:741px">Standard Room</div>
  <div class="room-desc" style="left:201px">Lorem ipsum dolor sit amet, consectetur adipiscing elit, sed do eiusmod tempor labore et</div>
  <div class="room-desc" style="left:470px">Lorem ipsum dolor sit amet, consectetur adipiscing elit, sed do eiusmod tempor labore et</div>
  <div class="room-desc" style="left:741px">Lorem ipsum dolor sit amet, consectetur adipiscing elit, sed do eiusmod tempor labore et</div>
  <div class="room-price" style="left:197px">Rs.490.00/ Night</div>
  <div class="room-price" style="left:467px">Rs.490.00/ Night</div>
  <div class="room-price" style="left:737px">Rs.490.00/ Night</div>

  <div class="dots" style="top:3273px"><span></span><span class="on"></span><span></span><span></span></div>
  <div class="btn-outline" style="left:530px;top:3323px;width:138px;height:38px">BOOK NOW</div>
</section>

<!-- Testimonial -->
<section>
  <p class="quote">“Lorem ipsum dolor sit amet, consectetur adipiscing elit, sed do eiusmod<br>tempor incididunt ut labore et dolore magna aliqua. Ut enim ad „</p>
  <div class="quote-name">Aren Colby</div>
  <div class="abs" style="left:560px;top:3553px;width:80px;height:80px;border-radius:50%;border:3px solid #f1f1f1;background:linear-gradient(180deg,#e9eef2,#b9c6d0)" role="img" aria-label="Guest portrait"></div>
</section>

<!-- Footer -->
<footer class="footer">
  <svg class="abs" style="left:516px;top:78px" width="165" height="122" viewBox="0 0 165 122" fill="none" stroke="#8a8a8a" stroke-width="1.2"><path d="M0 12V0h12M153 0h12v12M165 110v12h-12M12 122H0v-12"/></svg>
  <div class="footer-brand">Saffron Ridge</div>
  <div class="news">Subscribe our Newsletter</div>
  <div class="news-input">Enter Your Email
    <svg class="abs" style="right:14px;top:9px" width="14" height="14" viewBox="0 0 14 14"><path d="M1 6 13 1 9 13 7 8z" fill="#ffffff"/></svg>
  </div>
  <div class="socials"><span></span><span></span><span class="hl"></span><span></span></div>
  <div class="copy">copyright 2022 all rights reserved</div>
</footer>

</body>
</html>
```